Brightmoor Vector Systems Website

I am starting an IT consulting business called Brightmoor Vector Systems. I recently completed a logo contest on ArtHive and am now looking to put together a basic website. I can provide text and content but am looking for a site design with layout and graphics. I am attaching my logo below. I was thinking of a dark blue and white theme for the website (similar to the logo). However, I am open to ideas. Graphics can be a mix of business and high tech as that is the image I am trying to convey. The site will be relatively simple and probably have only 3 - 5 pages (Home, About Us, Services, Contact, etc.)
Target Market(s)
United States commercial companies and government contractors
Industry/Entity Type
Consulting

```html
<!DOCTYPE html>
<html lang="en">
<head>
<meta charset="utf-8">
<title>Brightmoor Vector Systems</title>
<link rel="stylesheet" href="https://fonts.googleapis.com/css2?family=Catamaran:wght@700;800&family=Roboto:wght@400;500;700&display=swap">
<style>
:root{
  --navy:#020a2a;
  --deep:#06194f;
  --blue:#0a56b0;
  --bright:#0b74d1;
  --sky:#2a8de0;
  --ink:#1b1f33;
  --grey:#7b7f8a;
  --white:#ffffff;
  --footer:#1d2238;
}
*{margin:0;padding:0;box-sizing:border-box}
html,body{width:1200px;height:2688px;overflow:hidden}
body{font-family:"Roboto",Arial,sans-serif;background:var(--white);position:relative}
.brand{position:absolute;display:flex;align-items:center;gap:10px;color:var(--white);font-family:"Roboto",Arial,sans-serif;font-weight:500;letter-spacing:1px}
.brand .dot{width:22px;height:22px;border-radius:50%;background:var(--sky)}
.hero{position:absolute;left:0;top:0;width:1200px;height:647px;
  background:radial-gradient(ellipse 520px 160px at 600px 40px,#1b5fb8 0%,transparent 100%),
  radial-gradient(ellipse 900px 180px at 600px 450px,#4a3fa0 0%,transparent 100%),
  linear-gradient(#031033 0%,#041a52 45%,#15205e 65%,#030b2a 100%)}
.hero .brand{left:144px;top:52px;font-size:24px}
.nav{position:absolute;top:56px;left:582px;display:flex;gap:29px;font-size:16px;color:var(--white)}
.nav a{color:inherit;text-decoration:none;position:relative}
.nav a.current{color:#cfe6ff}
.nav a.current:after{content:"";position:absolute;left:0;right:0;bottom:-9px;height:3px;background:var(--bright)}
.btn{position:absolute;display:flex;align-items:center;justify-content:space-between;background:var(--blue);color:var(--white);
  font-weight:500;border-radius:40px;padding:0 8px 0 24px}
.btn .ico{width:44px;height:44px;border-radius:50%;background:var(--white);display:flex;align-items:center;justify-content:center}
.login{left:945px;top:44px;width:110px;height:45px;font-size:15px;padding:0 4px 0 17px}
.login .ico{width:37px;height:37px}
.hero-title{position:absolute;left:0;width:1200px;text-align:center;font-family:"Catamaran",sans-serif;font-weight:800;color:var(--white);line-height:1}
.hero-title.l1{top:252px;font-size:62px}
.hero-title.l1 span{color:var(--bright)}
.hero-title.l2{top:330px;font-size:74px}
.start{left:492px;top:447px;width:216px;height:72px;font-size:20px}
.dots{position:absolute;left:1134px;top:351px;display:flex;flex-direction:column;gap:10px}
.dots i{width:8px;height:8px;border-radius:50%;background:var(--white)}
.dots i.on{background:var(--sky)}
.about{position:absolute;left:0;top:647px;width:1200px;height:584px}
.about h2{position:absolute;left:144px;top:82px;font-family:"Catamaran",sans-serif;font-weight:800;font-size:58px;color:var(--blue);line-height:1}
.about p{position:absolute;left:144px;top:172px;width:412px;font-size:13.5px;line-height:26.4px;color:var(--grey)}
.readmore{left:144px;top:424px;width:216px;height:72px;font-size:20px}
.vision{position:absolute;left:600px;top:0;width:600px;height:584px;
  background:radial-gradient(circle at 325px 250px,#3a9cff 0%,#0d4fa8 30%,#06214f 65%,#020b22 100%)}
.services{position:absolute;left:0;top:1231px;width:1200px;height:658px;
  background:linear-gradient(120deg,#eef3fa 0%,#dfe7f2 45%,#eef2f8 100%)}
.services h2{position:absolute;left:0;width:1200px;top:96px;text-align:center;font-family:"Catamaran",sans-serif;font-weight:800;font-size:56px;color:var(--blue);line-height:1}
.card{position:absolute;text-align:center}
.card h3{font-size:16px;font-weight:500;color:var(--ink)}
.card p{font-size:12.5px;line-height:24px;color:var(--grey);margin-top:12px}
.card.feature h3{color:var(--white);font-size:17px}
.card.feature p{color:var(--white);font-size:13px;line-height:25.5px}
.arrow{position:absolute;top:1578px}
.contact{position:absolute;left:0;top:1889px;width:1200px;height:638px;
  background:linear-gradient(#1565c6 0%,#0b4ea8 40%,#073178 75%,#02102e 100%)}
.contact h2{position:absolute;left:0;width:1200px;top:78px;text-align:center;font-family:"Catamaran",sans-serif;font-weight:800;font-size:56px;color:var(--white);line-height:1}
.field{position:absolute;background:var(--white);font-size:16px;color:#555a66;padding:18px 21px}
.submit{left:460px;top:478px;width:279px;height:73px;font-size:20px}
.footer{position:absolute;left:0;top:2527px;width:1200px;height:161px;background:var(--footer)}
.footer .brand{left:144px;top:44px;font-size:26px}
.fnav{position:absolute;left:575px;top:48px;display:flex;gap:20px;color:var(--white);font-size:19px;font-weight:500}
.copy{position:absolute;left:575px;top:94px;color:var(--white);font-size:11px}
</style>
</head>
<body>

<section class="hero" role="img" aria-label="Dark blue high tech backdrop with a glowing wave of dots">
  <div class="brand"><span class="dot"></span>Brightmoor Vector Systems</div>
  <nav class="nav">
    <a class="current">Home</a><a>About Us</a><a>Services</a><a>Contact</a>
  </nav>
  <div class="btn login">LOGIN<span class="ico"><svg width="16" height="16" viewBox="0 0 16 16"><path d="M5 3l6 5-6 5" fill="none" stroke="#0a56b0" stroke-width="2.4"/></svg></span></div>
  <div class="hero-title l1">BRIGHTMOOR <span>VECTOR</span></div>
  <div class="hero-title l2">SYSTEMS</div>
  <div class="btn start">GET STARTED<span class="ico"><svg width="18" height="18" viewBox="0 0 16 16"><path d="M5 3l6 5-6 5" fill="none" stroke="#0a56b0" stroke-width="2.4"/></svg></span></div>
  <div class="dots"><i></i><i></i><i class="on"></i><i></i><i></i></div>
</section>

<section class="about">
  <h2>ABOUT US</h2>
  <p>Lorem ipsum dolor sit amet, consectetur adipiscind do eiusmod tempor incididunt ut labore et doloquis ipsum suspendisse ultrices gravidommodo viverra maecenas accumsan lacus vel facilisisorem ipsum dolor sit amet, consectetur adipiscing elit, sed do eiusmod tempor incididunt ut labore et dolore magna aliquis isuspendisse ultrices gravidommodo viverra maecenas accumsan lacus vel facilisisem ipsum dolor sit amet, consectetur adipiscing elit, sed do eiusmod tempor incididunt ut labore et dolore magna</p>
  <div class="btn readmore">READ MORE<span class="ico"><svg width="18" height="18" viewBox="0 0 16 16"><path d="M5 3l6 5-6 5" fill="none" stroke="#0a56b0" stroke-width="2.4"/></svg></span></div>
  <div class="vision" role="img" aria-label="Photo of a hand touching a glowing digital interface reading Our Vision"></div>
</section>

<section class="services" role="img" aria-label="Faded photo of business people shaking hands behind the services">
  <h2>OUR SERVICES</h2>
  <svg width="1200" height="658" style="position:absolute;left:0;top:0">
    <g fill="none">
      <circle cx="311" cy="381" r="140" stroke="#0b74d1" stroke-width="9"/>
      <path d="M214 280 A140 140 0 0 1 408 280" stroke="#1b1f33" stroke-width="9"/>
      <circle cx="311" cy="381" r="128" fill="#fff" stroke="#e8edf4" stroke-width="2"/>
      <circle cx="889" cy="381" r="140" stroke="#0b74d1" stroke-width="9"/>
      <path d="M792 280 A140 140 0 0 1 986 280" stroke="#1b1f33" stroke-width="9"/>
      <circle cx="889" cy="381" r="128" fill="#fff" stroke="#e8edf4" stroke-width="2"/>
      <circle cx="600" cy="381" r="168" fill="#fff"/>
      <circle cx="600" cy="381" r="168" stroke="#0b74d1" stroke-width="10"/>
      <path d="M485 258 A168 168 0 0 1 715 258" stroke="#1b1f33" stroke-width="10"/>
      <circle cx="600" cy="381" r="152" fill="#0b74d1"/>
    </g>
    <g fill="none" stroke="#0a56b0" stroke-width="2.5">
      <circle cx="320" cy="294" r="18"/><path d="M282 322h30l18-10M282 318v16"/>
      <rect x="860" y="279" width="56" height="40" rx="3"/><path d="M870 292h36M870 302h30"/>
    </g>
    <g fill="none" stroke="#fff" stroke-width="2.5">
      <circle cx="600" cy="280" r="14"/><circle cx="578" cy="310" r="8"/><circle cx="622" cy="310" r="8"/>
      <path d="M568 330v-8h20v8M612 330v-8h20v8"/>
    </g>
  </svg>
  <div class="card" style="left:211px;top:370px;width:200px"><h3>QUAENVENTORE</h3><p>Lorem ipsum dolor sit onsectetur adipiscing elit, sed do eiusmod tempor incididuntlabore</p></div>
  <div class="card feature" style="left:480px;top:358px;width:240px"><h3>ED QUIA NON NUM</h3><p>Lorem ipsum dolor sit onsectetur adipiscing elit, sed do eiusmod tempor incididuntlabore elore magna aliqua.</p></div>
  <div class="card" style="left:789px;top:370px;width:200px"><h3>TEMPORA INCIDU</h3><p>Lorem ipsum dolor sit onsectetur adipiscing elit, sed do eiusmod tempor incididuntlabore</p></div>
</section>
<svg class="arrow" style="left:88px" width="36" height="68" viewBox="0 0 36 68"><path d="M34 2L2 34l32 32" fill="none" stroke="#8a96ab" stroke-width="1.5"/></svg>
<svg class="arrow" style="left:1076px" width="36" height="68" viewBox="0 0 36 68"><path d="M2 2l32 32L2 66" fill="none" stroke="#8a96ab" stroke-width="1.5"/></svg>

<section class="contact" role="img" aria-label="Blue background with a network of connected glowing dots">
  <h2>CONTACT FORM</h2>
  <div class="field" style="left:234px;top:194px;width:359px;height:51px">First Name</div>
  <div class="field" style="left:605px;top:194px;width:360px;height:51px">Last Name</div>
  <div class="field" style="left:234px;top:259px;width:360px;height:51px">Email address</div>
  <div class="field" style="left:605px;top:259px;width:360px;height:51px">Phone Number</div>
  <div class="field" style="left:234px;top:323px;width:731px;height:115px">Message</div>
  <div class="btn submit">SUBMIT MESSAGE<span class="ico"><svg width="18" height="18" viewBox="0 0 16 16"><path d="M5 3l6 5-6 5" fill="none" stroke="#0a56b0" stroke-width="2.4"/></svg></span></div>
</section>

<footer class="footer">
  <div class="brand"><span class="dot"></span>Brightmoor Vector Systems</div>
  <div class="fnav"><span>HOME</span><span>/</span><span>ABOUT US</span><span>/</span><span>SERVICES</span><span>/</span><span>CONTACT</span></div>
  <div class="copy">© 2021 Brightmoor Vector Systems. All rights reserved.Privacy Terms of Use</div>
</footer>

</body>
</html>
```